Funky Retro Membership Brochure

We require an A5 (A4 folded) brochure design that outlines the membership options for CoveChat. CoveChat promotes local businesses via social media and presence on the CoveChat website (www.covechat-example.com.au) as well as providing networking facilities for the local business to meet and collaborate with each other.

Attached are the various Covechat logos together with the colour style guide. Please ignore the fonts; just note the colours.

We would like the brochure to have a retro style look. Very funky but professional.

The first page of the brochure is the title page. Logo with the following tagline "Linking and Lifting Local Traders in Sydney's Inner West". Additional Text, "2020 Membership". Please also include"#covechat" on the title page. This hashtag should be in a retro font on an angle.

The second page refers to what we do. Three section headings and text as follows but will require designers to provide appropriate graphics, for example the CoveChat website inside a computer screen etc.:

COVECHAT WEBSITE
covechat-example.com.au is the online, digital showcase of our members and their business. Each member has a dedicated webpage to promote their business. Your member page provides all you contact details, links and social media channels, reviews, logos and more.

HARBOURMEET
HarbourMeet is where CoveChat members get together. It’s a business community unlike any other. No selling. No Pressure. And it won’t break the bank. We aim to stop the isolation many business owners feel and encourage genuine connections, where referrals happen naturally.

SOCIAL MEDIA
CoveChat uses social media channels to actively promote the CoveChat community and its members. Not only do we promote the businesses but also provide free promotions and advertising for local community groups, schools and non-for-profit organisations.

The third page provides details of the membership levels and annual fees. The information on the membership categories can be found at https://www.covechat-example.com.au/membership-levels/ All the information contained on the page should be contained on page three of the brochure.

The final, back page, will contain all of the contact details for CoveChat (also found on the www.covechat-example.com.au)

Target Market(s)

Local community businesses

Industry/Entity Type

Digital Marketing

Font styles to use
Other font styles liked:
• Retro

Requirements
Must have
• Retro feel - refer to project description
Nice to have
• Refer to project description
Should not have
• Not applicable

```html
<!DOCTYPE html>
<html lang="en">
<head>
<meta charset="utf-8">
<title>CoveChat — 2020 Membership</title>
<link rel="stylesheet" href="https://fonts.googleapis.com/css2?family=Staatliches&family=Playfair+Display:ital,wght@1,700;1,900&family=Roboto:wght@500&display=swap">
<style>
  :root {
    --sepia-dark: #c9a88a;
    --sepia-mid: #dcc2a9;
    --sepia-light: #efe4d8;
    --cove-blue: #5a9fbd;
    --cove-slate: #546173;
    --paper: #f5f0ec;
    --white: #ffffff;
  }
  * { margin: 0; padding: 0; box-sizing: border-box; }
  html, body { width: 846px; height: 1200px; overflow: hidden; }
  body { background: var(--sepia-light); }
  .cover {
    position: relative;
    width: 846px;
    height: 1200px;
    overflow: hidden;
  }
  .cover__backdrop {
    position: absolute;
    inset: 0;
    background:
      radial-gradient(ellipse 260px 340px at 140px 420px, rgba(176,136,104,.55), transparent 70%),
      radial-gradient(ellipse 200px 300px at 470px 650px, rgba(176,136,104,.45), transparent 70%),
      radial-gradient(ellipse 160px 420px at 700px 760px, rgba(190,150,118,.35), transparent 70%),
      radial-gradient(ellipse 420px 300px at 560px 180px, rgba(245,236,226,.8), transparent 70%),
      linear-gradient(160deg, var(--sepia-mid) 0%, var(--sepia-light) 55%, var(--sepia-mid) 100%);
  }
  .brand {
    position: absolute;
    top: 31px;
    left: 0;
    width: 846px;
    display: flex;
    justify-content: center;
    align-items: center;
    gap: 16px;
  }
  .brand__dot {
    width: 86px;
    height: 86px;
    border-radius: 50%;
    background: var(--white);
  }
  .brand__name {
    font-family: "Roboto", sans-serif;
    font-weight: 500;
    font-size: 50px;
    letter-spacing: 1px;
    color: var(--cove-slate);
  }
  .tagline {
    position: absolute;
    top: 206px;
    left: 0;
    width: 846px;
    text-align: center;
    font-family: "Staatliches", sans-serif;
    font-size: 96px;
    line-height: 106px;
    letter-spacing: 1px;
  }
  .tagline__line { display: block; }
  .tagline__line--blue { color: var(--cove-blue); }
  .tagline__line--slate { color: var(--cove-slate); }
  .edition {
    position: absolute;
    left: 170px;
    top: 817px;
    width: 504px;
    height: 94px;
  }
  .edition svg { position: absolute; inset: 0; }
  .edition__text {
    position: absolute;
    inset: 0;
    display: flex;
    justify-content: center;
    align-items: center;
    gap: 12px;
    font-family: "Playfair Display", serif;
    font-style: italic;
    font-weight: 900;
    font-size: 40px;
    color: var(--cove-slate);
    text-transform: uppercase;
  }
  .edition__word::first-letter { font-size: 58px; }
  .hashtag-band { position: absolute; inset: 0; pointer-events: none; }
  .hashtag {
    position: absolute;
    left: 757px;
    top: 1113px;
    transform: translate(-50%, -50%) rotate(-45deg);
    font-family: "Staatliches", sans-serif;
    font-size: 40px;
    color: var(--cove-slate);
    white-space: nowrap;
  }
</style>
</head>
<body>
  <main class="cover">
    <div class="cover__backdrop" role="img" aria-label="Sepia-toned photograph of a vintage telephone handset with coiled cord"></div>

    <header class="brand">
      <span class="brand__dot"></span>
      <span class="brand__name">COVECHAT</span>
    </header>

    <h1 class="tagline">
      <span class="tagline__line tagline__line--blue">Linking</span>
      <span class="tagline__line tagline__line--slate">and</span>
      <span class="tagline__line tagline__line--blue">Lifting</span>
      <span class="tagline__line tagline__line--slate">Local Traders in</span>
      <span class="tagline__line tagline__line--blue">Sydney’s Inner West</span>
    </h1>

    <div class="edition">
      <svg width="504" height="94" viewBox="0 0 504 94">
        <path d="M24 1 H480 Q480 24 503 24 V70 Q480 70 480 93 H24 Q24 70 1 70 V24 Q24 24 24 1 Z"
              fill="rgba(245,240,236,.88)" stroke="#546173" stroke-width="2"/>
      </svg>
      <p class="edition__text"><span>2020</span><span class="edition__word">Membership</span></p>
    </div>

    <svg class="hashtag-band" width="846" height="1200" viewBox="0 0 846 1200">
      <polygon points="626,1200 846,980 846,1068 714,1200" fill="#ffffff"/>
    </svg>
    <p class="hashtag">#COVECHAT</p>
  </main>
</body>
</html>
```